Construction Company informative web page

Lorvane Builders is a new company that combine Project Manager and kitchen & bath design with Interior remodeling for houses or business (commercial and residential construction)
We want to show our reviews, portafolio and background experience
Updates

Reason: I would like to have the time to interact with the favorite designers to fine tune the website also I'd like to see more designs

Hello Everybody,

Thank you for your time, please make the corrections shown below:

Pages:

1. Home:

1.  Includes a welcome and a briefly background:

2. Right side vertically show a few reviews with the option read more to open it, just the Name and last name, city and review (no start ratings)

3. Facebook and youtube link

4. Left side below shows 4 slides show with pictures and titles:

1. Kitchen Design

2. Bath Design

3. General Remodeling

4. Commercial Projects

2. About Us:

Our Professionals:

Lorvane Builders Project Manager  is responsible to set the project schedule, request materials  and coordinate the delivery on time.  The Project Manager focus is ensuring  the best customer satisfaction in every step of the project until the final product is completed.

The Designer gives you the best ideas in 3D format,   getting the best lay out possible.  understanding your needs, defining your unique style putting together all your requirements and ideas to make the best match for you, making sure you get the best products within your budget

Lorvane Builders have a high quality group of trade specialist; plumbers, electricians and installers. Our crew is pleasant to work with,  safety and cleaning values  and very detailed oriented

Our Core Values

As our slogan your project is our business, well we really mean it our job is not just to do the job is to guaranteed a pleasant experience with great costumer service, communication, quality, in time and within your budget

 

1. Services:

1. Commercial

2. Residential

2. Portafolio:  Separated pictures in each project, I want to have a brief description in each picture

1. Kitchen Design

2. Bath Design

3. General Remodeling

4. Commercial Projects

 

1. Contact Us:  

1. Project Management Department:

Contact Person: Tessa Kobrin

Email: tessa@lorvanebuilders.com

2. Office Management Department:

Contact Person: Rue Fendwick

Email: info@lorvanebuilders.com

 

Please try to pick design style shown in business card to match a little bit. Keep the color tones

I want the logo in the upper left corner and a very nice picture with a kitchen (warm colors)mostly American northeast style like the main pic of the web.

I want the web page is able to be fully open in computers, tablets and cellphones

Please send me an email to lorvanebuild7@mailbrook.net so I can send you my logo and any other information to be incorporated

Thank you

Hello Everybody,

Thank you for your time, please make the corrections accordingly:

Pages:

1. Home: Includes a welcome and a briefly say something about our background 

Hello, I just upload my logo and my business card so you can adjust your designs

Please presented responsive format

I want coding the webpage too

Please read carefully my last update

Thank you so much!                                   

Industry/Entity Type

Residential

Requirements
Nice to have
• Should it has a Newsletter subscription with the email at the bottom of the home page
In contact page: A box "Contact us for a free estimate"

```html
<!DOCTYPE html>
<html lang="en">
<head>
<meta charset="utf-8">
<title>Lorvane Builders</title>
<link href="https://fonts.googleapis.com/css2?family=Oswald:wght@300;400;500&family=Open+Sans:wght@400;600&display=swap" rel="stylesheet">
<style>
:root{
  --wine:#7a2320;
  --wine-field:#843a2f;
  --rose:#b56361;
  --rose-dark:#a4514f;
  --tan:#e2c283;
  --tan-light:#efd9a9;
  --band:#e4c58b;
  --cream:#f3efe0;
  --ivory:#f7eed8;
  --ink:#3c3c3c;
  --text:#4a4a4a;
  --nav-text:#7a5a45;
  --bronze:#8a5c47;
}
*{margin:0;padding:0;box-sizing:border-box}
html,body{width:900px;height:1200px;overflow:hidden}
body{position:relative;background:linear-gradient(var(--band) 0 72px,var(--cream) 72px);font-family:"Open Sans",sans-serif;color:var(--text)}
.abs{position:absolute}
.topbar{left:15px;top:14px;width:870px;height:83px;background:var(--wine);border-radius:4px;box-shadow:0 3px 6px rgba(0,0,0,.25)}
.brand{left:16px;top:22px;display:flex;align-items:center;gap:8px}
.brand-mark{width:18px;height:18px;background:var(--ivory)}
.brand-name{font-family:"Oswald",sans-serif;font-weight:400;font-size:17px;color:var(--ivory);width:80px;line-height:20px}
.divider{left:112px;top:12px;width:1px;height:58px;background:rgba(255,255,255,.25)}
.call{left:143px;top:26px;display:flex;align-items:center;gap:10px;font-family:"Oswald",sans-serif;color:var(--ivory)}
.call strong{font-weight:400;font-size:22px}
.call span{font-weight:300;font-size:21px}
.social{top:21px;width:41px;height:41px;border-radius:50%;background:var(--ivory)}
.nav{left:15px;top:122px;width:870px;height:46px;background:linear-gradient(var(--tan-light),var(--tan));border:1px solid #d9b978;border-radius:3px 3px 0 0;display:flex}
.nav a{font-family:"Oswald",sans-serif;font-size:17px;color:var(--nav-text);text-decoration:none;text-transform:uppercase;border-right:1px solid #cfae70;line-height:44px;text-align:center}
.nav a.current{color:var(--wine)}
.hero{left:15px;top:167px;width:870px;height:347px;background:linear-gradient(100deg,#5c3a28,#a26a40 30%,#7d4a30 55%,#b37a4d 75%,#6a3528)}
.hero-caption{left:15px;top:398px;width:354px;height:50px;background:rgba(230,201,140,.88);font-family:"Oswald",sans-serif;font-size:26px;color:var(--wine);line-height:50px;padding-left:26px}
.slide-btn{top:475px;width:34px;height:34px;background:var(--wine);color:#fff;font-size:20px;font-weight:600;text-align:center;line-height:33px}
.welcome{left:15px;top:514px;width:870px;height:231px;background:#f8f8f6}
.welcome-text{left:30px;top:530px;width:600px;text-align:center}
.welcome-text h1{font-family:"Oswald",sans-serif;font-weight:400;font-size:31px;color:var(--ink)}
.welcome-text h1 em{font-style:normal;color:var(--wine)}
.welcome-text h2{font-weight:400;font-size:21px;color:#555;letter-spacing:.5px;margin-top:6px}
.rule{height:2px;margin:12px 40px 0;background:linear-gradient(90deg,transparent,#bbb,transparent)}
.welcome-text p{font-family:Arial,sans-serif;font-size:14px;line-height:20px;color:#444;margin-top:14px}
.welcome-text p b{font-weight:400;color:var(--wine)}
.learn{margin-top:14px;font-family:"Oswald",sans-serif;font-weight:300;font-size:20px;color:#7a4a3a;display:inline-flex;align-items:center;gap:8px}
.estimate{left:645px;top:196px;width:229px;height:515px;background:var(--tan);box-shadow:0 1px 3px rgba(0,0,0,.25)}
.estimate-head{height:116px;background:var(--wine);font-family:"Oswald",sans-serif;font-size:14px;color:#fff;text-align:center;line-height:20px;padding:11px 16px}
.estimate label{display:block;font-size:14px;color:var(--wine);margin:12px 0 3px 12px}
.field{margin-left:12px;width:205px;height:31px;background:var(--wine-field);color:var(--tan-light);font-size:13px;line-height:31px;padding-left:10px;display:flex;align-items:center;gap:10px}
.field.tall{height:64px}
.submit{position:absolute;left:62px;top:473px;width:104px;height:33px;border-radius:4px;background:linear-gradient(#3a3a3a,#050505);color:#fff;font-size:16px;text-align:center;line-height:33px}
.card{top:773px;width:272px;height:364px}
.card-title{height:48px;background:#fafafa;font-family:"Oswald",sans-serif;font-weight:300;font-size:21px;color:var(--ink);text-transform:uppercase;line-height:50px;padding-left:14px}
.tile{position:relative;height:138px;margin-top:2px}
.tile span{position:absolute;left:0;bottom:0;width:100%;height:32px;background:rgba(30,30,30,.72);color:#fff;font-size:16px;text-align:center;line-height:32px}
.see-all{height:36px;margin-top:1px;background:var(--bronze);color:#fff;font-size:18px;line-height:36px;padding:0 14px;display:flex;justify-content:space-between;align-items:center}
.reviews{left:613px;top:773px;width:272px;height:364px;background:var(--rose)}
.reviews-title{height:48px;background:var(--rose-dark);font-family:"Oswald",sans-serif;font-weight:300;font-size:21px;color:var(--ivory);line-height:50px;padding-left:18px}
.review{border-top:1px solid rgba(255,255,255,.35);color:#fff;font-size:16px;padding:0 10px 0 18px;display:flex;justify-content:space-between;align-items:center}
.review.open{background:var(--tan);color:var(--wine);display:block;padding-top:10px}
.review.open .row{display:flex;justify-content:space-between;align-items:center}
.review.open p{font-size:13px;color:#222;line-height:20px;margin-top:4px}
.footer{left:0;top:1165px;width:900px;height:35px;background:var(--wine);color:#fff;font-size:13px;line-height:35px;padding:0 15px;display:flex;justify-content:space-between}
</style>
</head>
<body>
<header class="abs topbar">
  <div class="abs brand"><div class="brand-mark"></div><div class="brand-name">Lorvane Builders</div></div>
  <div class="abs divider"></div>
  <div class="abs call">
    <svg width="17" height="17" viewBox="0 0 24 24" aria-hidden="true"><path fill="#f7eed8" d="M6.6 10.8a15.1 15.1 0 0 0 6.6 6.6l2.2-2.2c.3-.3.7-.4 1-.2 1.1.4 2.3.6 3.6.6.6 0 1 .4 1 1V20c0 .6-.4 1-1 1A17 17 0 0 1 3 4c0-.6.4-1 1-1h3.5c.6 0 1 .4 1 1 0 1.3.2 2.5.6 3.6.1.3 0 .7-.2 1z"/></svg>
    <strong>FEEL FREE TO CALL US!</strong><span>+215-555-0147</span>
  </div>
  <a class="abs social" style="left:711px" aria-label="Social page one"></a>
  <a class="abs social" style="left:763px" aria-label="Social page two"></a>
  <a class="abs social" style="left:814px" aria-label="Social page three"></a>
</header>

<nav class="abs nav">
  <a class="current" style="width:98px">Home</a>
  <a style="width:108px">About</a>
  <a style="width:124px">Features</a>
  <a style="width:131px">Protfolio</a>
  <a style="width:94px">Blog</a>
  <a style="width:122px">Contact</a>
</nav>

<div class="abs hero" role="img" aria-label="Warm wood kitchen with granite island, bar stools and pendant lights"></div>
<div class="abs hero-caption">LOREM IPSUM &amp; DOLOR AMET!</div>
<div class="abs slide-btn" style="left:561px">&#10094;</div>
<div class="abs slide-btn" style="left:601px">&#10095;</div>

<section class="abs welcome"></section>
<div class="abs welcome-text">
  <h1>Welcome to <em>Lorvane Builders</em> Website</h1>
  <h2>simply dummy text of the printing and typesetting.</h2>
  <div class="rule"></div>
  <p>It is a long established fact that a reader will be <b>distracted</b> by the readable content of a page<br>when looking at its layout. The point of using Lorem Ipsum is that it has a more-or-less as<br>opposed to using <b>'Content here, content here'</b>,</p>
  <span class="learn">learn more
    <svg width="19" height="19" viewBox="0 0 20 20" aria-hidden="true"><circle cx="10" cy="10" r="9" fill="#8a5c47"/><path d="M5 10h8M10 6l4 4-4 4" stroke="#fff" stroke-width="2.2" fill="none"/></svg>
  </span>
</div>

<form class="abs estimate">
  <div class="estimate-head">Ask an appointment for a free estimate or contact any of our specialist if you have any question or need any help in your project</div>
  <label>Name:</label><div class="field"></div>
  <label style="margin-top:13px">Best number to reach you:</label><div class="field"></div>
  <label style="margin-top:14px">Description of your project:</label><div class="field tall"></div>
  <label>Appointments date</label>
  <div class="field"><svg width="18" height="18" viewBox="0 0 18 18" aria-hidden="true"><rect x="1" y="2" width="16" height="15" fill="none" stroke="#efd9a9"/><path d="M1 6h16M5 0v4M13 0v4M4 9h2M8 9h2M12 9h2M4 13h2M8 13h2M12 13h2" stroke="#efd9a9"/></svg>03/24/2014</div>
  <label>Appointments time</label><div class="field">10.20 am</div>
  <div class="submit">Submit</div>
</form>

<section class="abs card" style="left:16px">
  <div class="card-title">Portafolio</div>
  <div class="tile" role="img" aria-label="White bathroom with tub and sink" style="background:linear-gradient(135deg,#e6e2dc,#b9b3aa)"><span>Variations of Passages</span></div>
  <div class="tile" role="img" aria-label="Kitchen with white cabinets and dark counter" style="background:linear-gradient(135deg,#d8d6d2,#5a5550)"><span>Established Fact</span></div>
  <div class="see-all">See All <svg width="22" height="22" viewBox="0 0 20 20" aria-hidden="true"><circle cx="10" cy="10" r="9.5" fill="#f7eed8"/><path d="M8 5l5 5-5 5" stroke="#8a5c47" stroke-width="2.4" fill="none"/></svg></div>
</section>

<section class="abs card" style="left:315px">
  <div class="card-title">Background Experience</div>
  <div class="tile" role="img" aria-label="Kitchen with wood cabinets and red tile backsplash" style="background:linear-gradient(135deg,#4e3526,#9a5a3a 55%,#3a2a20)"><span>Specimen Book</span></div>
  <div class="tile" role="img" aria-label="Bathroom with purple walls and white tub" style="background:linear-gradient(135deg,#eceaf0,#6d5f86)"><span>Lorem Ipsum Available</span></div>
  <div class="see-all">See All <svg width="22" height="22" viewBox="0 0 20 20" aria-hidden="true"><circle cx="10" cy="10" r="9.5" fill="#f7eed8"/><path d="M8 5l5 5-5 5" stroke="#8a5c47" stroke-width="2.4" fill="none"/></svg></div>
</section>

<section class="abs reviews">
  <div class="reviews-title">REVIEWS</div>
  <div class="review" style="height:44px">Lorem Ipsum used since <svg width="20" height="20" viewBox="0 0 20 20" aria-hidden="true"><circle cx="10" cy="10" r="10" fill="#f7eed8"/><path d="M5 10h10M10 5v10" stroke="#b56361" stroke-width="2.5"/></svg></div>
  <div class="review open" style="height:89px">
    <div class="row">Lorem Ipsum used since <svg width="20" height="20" viewBox="0 0 20 20" aria-hidden="true"><circle cx="10" cy="10" r="10" fill="#f7eed8"/><path d="M5 10h10" stroke="#b56361" stroke-width="2.5"/></svg></div>
    <p>Lorem ipsum dolor sit amet conse<br>ctetur adipisicing elit,</p>
  </div>
  <div class="review" style="height:43px">Lorem Ipsum used since <svg width="20" height="20" viewBox="0 0 20 20" aria-hidden="true"><circle cx="10" cy="10" r="10" fill="#f7eed8"/><path d="M5 10h10M10 5v10" stroke="#b56361" stroke-width="2.5"/></svg></div>
  <div class="review" style="height:44px">Lorem Ipsum used since <svg width="20" height="20" viewBox="0 0 20 20" aria-hidden="true"><circle cx="10" cy="10" r="10" fill="#f7eed8"/><path d="M5 10h10M10 5v10" stroke="#b56361" stroke-width="2.5"/></svg></div>
  <div class="review" style="height:46px">Lorem Ipsum used since <svg width="20" height="20" viewBox="0 0 20 20" aria-hidden="true"><circle cx="10" cy="10" r="10" fill="#f7eed8"/><path d="M5 10h10M10 5v10" stroke="#b56361" stroke-width="2.5"/></svg></div>
  <div class="review" style="height:48px">Lorem Ipsum used since <svg width="20" height="20" viewBox="0 0 20 20" aria-hidden="true"><circle cx="10" cy="10" r="10" fill="#f7eed8"/><path d="M5 10h10M10 5v10" stroke="#b56361" stroke-width="2.5"/></svg></div>
</section>

<footer class="abs footer">
  <span>Lorvane Builders © 2014. Privacy Policy</span>
  <span>Designed &amp; Developed by Brindle Webworks.</span>
</footer>
</body>
</html>
```